Business Card Design

Extremely classy understated design.

Printing in fancy scrip or hand writing.

Conservative color scheme such as black print on beige paper. I am sure you have much better ideas than I would have.

I am involved in a number of different businesses and require a simple elegant business card.

I would like a object on the card, such as, a bald eagle, an antique Calloway Vance, a water fall or a beautiful flower.

My name is: Gerald T. Whitlock Not Gerald T. Whitlock Investments Investments is my occupation Most of the designs are not acceptable. Very disappointed with results.

Industry/Entity Type

Business

Contact Information for Business Card

Gerald T Whitlock
Investments
555 214 6093
mervinlk@postbay.net

```html
<!DOCTYPE html>
<html lang="en">
<head>
<meta charset="utf-8">
<title>Gerald T Whitlock — Business Card</title>
<link rel="stylesheet" href="https://fonts.googleapis.com/css2?family=Jost:wght@400;500&display=swap">
<style>
  :root {
    --ink: #141414;
    --paper: #ffffff;
    --mist-dark: #8e8e8e;
    --mist-mid: #c9c9c9;
    --mist-light: #f4f4f4;
    --band-black: #0c0c0c;
    --band-grey: #5a5a5a;
    --sedan-dark: #2c2f33;
    --sedan-mid: #8a8d90;
  }
  * { margin: 0; padding: 0; box-sizing: border-box; }
  html, body { width: 1200px; height: 702px; overflow: hidden; background: var(--paper); }
  .card {
    position: relative;
    width: 1200px;
    height: 702px;
    overflow: hidden;
    background:
      radial-gradient(ellipse 70% 80% at 75% 60%, var(--paper) 0%, rgba(255,255,255,0) 70%),
      linear-gradient(160deg, var(--mist-dark) 0%, var(--mist-mid) 35%, var(--mist-light) 65%, var(--paper) 100%);
    font-family: "Jost", "Futura", sans-serif;
    color: var(--ink);
  }
  .sedan-photo {
    position: absolute;
    left: 84px;
    top: 222px;
    width: 790px;
    height: 370px;
    border-radius: 46% 54% 20% 20% / 40% 40% 18% 18%;
    background:
      radial-gradient(ellipse 60% 70% at 30% 55%, var(--sedan-dark) 0%, var(--sedan-mid) 55%, rgba(255,255,255,0) 100%);
    opacity: 0.95;
  }
  .wave-band {
    position: absolute;
    left: 0;
    bottom: 0;
    width: 1200px;
    height: 170px;
  }
  .identity {
    position: absolute;
    right: 74px;
    top: 112px;
    text-align: right;
    white-space: nowrap;
  }
  .identity__name {
    font-weight: 400;
    font-size: 62px;
    line-height: 1;
    letter-spacing: 0.5px;
  }
  .identity__occupation {
    font-weight: 400;
    font-size: 39px;
    line-height: 1.1;
    margin-top: 2px;
  }
  .contact {
    position: absolute;
    right: 74px;
    top: 290px;
    text-align: right;
    font-size: 25px;
    line-height: 36px;
    white-space: nowrap;
  }
</style>
</head>
<body>
  <div class="card">
    <div class="sedan-photo" role="img" aria-label="Photograph of a classic black luxury sedan"></div>

    <svg class="wave-band" viewBox="0 0 1200 170" preserveAspectRatio="none" aria-hidden="true">
      <defs>
        <linearGradient id="band-sheen" x1="0" y1="0" x2="0" y2="1">
          <stop offset="0" stop-color="#5a5a5a"/>
          <stop offset="1" stop-color="#0c0c0c"/>
        </linearGradient>
      </defs>
      <path d="M0 30 C 240 20, 420 60, 640 62 C 860 64, 1030 20, 1200 6 L1200 170 L0 170 Z" fill="#0c0c0c"/>
      <path d="M0 72 C 260 60, 440 96, 660 98 C 880 100, 1040 66, 1200 50 L1200 170 L0 170 Z" fill="url(#band-sheen)" opacity="0.55"/>
      <path d="M0 108 C 260 100, 460 126, 680 128 C 900 130, 1050 106, 1200 96 L1200 170 L0 170 Z" fill="#0c0c0c"/>
    </svg>

    <div class="identity">
      <div class="identity__name">Gerald T Whitlock</div>
      <div class="identity__occupation">Investments</div>
    </div>

    <div class="contact">
      <div class="contact__phone">555 214 6093</div>
      <div class="contact__email">mervinlk@postbay.net</div>
    </div>
  </div>
</body>
</html>
```